Tillard Environmental Projects New Website Design

I need a new website for a Environmental Project Company based in Sydney Australia, working throughout South East Asia.I've attached the company logo, please try & incorporate these colours or use complimentary colours. I've attached a word doc with design brief.I'm going to use Wix, so please ensure files are suitable.Thankyou.

Number of Pages Required

5+ page

Colors

Designer to choose colors to be used in the design.

Requirements
Must have
• Refer to Word Document
Nice to have
• Refer to Word Document
Should not have
• Not to be dark

```html
<!DOCTYPE html>
<html lang="en">
<head>
<meta charset="utf-8">
<title>Tillard Environmental Projects</title>
<link href="https://fonts.googleapis.com/css2?family=Montserrat:wght@400;600;700&family=Open+Sans:wght@400;600&display=swap" rel="stylesheet">
<style>
:root{
  --green:#7db533;
  --green-dark:#3a5a22;
  --teal:#169a6e;
  --charcoal:#363636;
  --ink:#222;
  --muted:#666;
  --paper:#f4f2f1;
  --white:#fff;
  --rule:#d8d8d8;
}
*{box-sizing:border-box;margin:0;padding:0}
html,body{width:1200px;height:5128px;overflow:hidden}
body{font-family:"Open Sans",Arial,sans-serif;color:var(--ink);background:var(--white)}
h1,h2,h3,h4,.btn,.nav a{font-family:Montserrat,Arial,sans-serif}

.site-header{height:113px;display:flex;align-items:center;justify-content:space-between;padding:0 40px 0 130px;background:var(--white)}
.brand{display:flex;align-items:center;gap:14px}
.brand-dot{width:66px;height:66px;border-radius:50%;background:var(--green-dark)}
.brand-name{font-family:Montserrat,Arial,sans-serif;font-weight:700;font-size:20px;line-height:1.1;color:var(--green-dark);text-transform:uppercase;width:190px}
.nav{display:flex;gap:22px}
.nav a{font-size:12px;font-weight:600;color:var(--ink);text-decoration:none;text-transform:uppercase}
.nav a.active{color:var(--green);border-bottom:2px solid var(--green);padding-bottom:6px}

.hero{position:relative;height:595px;background:linear-gradient(180deg,#b9c9d3 0%,#7f9a6c 45%,#46693a 100%)}
.hero-box{position:absolute;left:106px;top:349px;width:410px;height:154px;background:rgba(40,52,30,.78);padding:22px 22px}
.hero-box h1{color:var(--white);font-size:38px;line-height:1.05;font-weight:700}
.hero-dots{position:absolute;left:0;right:0;top:540px;display:flex;justify-content:center;gap:14px}
.hero-dots span{width:9px;height:9px;border-radius:50%;background:rgba(255,255,255,.7)}
.hero-dots span.on{background:var(--white);box-shadow:0 0 0 3px rgba(255,255,255,.4)}

.btn{display:inline-block;background:var(--green);color:var(--white);font-size:13px;font-weight:700;text-transform:uppercase;padding:10px 18px;text-decoration:none}
.btn-small{background:var(--white);color:var(--ink);font-size:11px;padding:7px 14px}

.band{background:var(--paper)}
.section-title{text-align:center;font-size:26px;font-weight:700;text-transform:uppercase;color:var(--ink)}
.services{height:1063px;padding-top:50px}
.products{height:1129px;padding-top:80px;background:var(--white)}
.card-grid{display:grid;grid-template-columns:repeat(4,256px);column-gap:38px;padding:0 31px;margin-top:52px}
.products .card-grid{margin-top:70px}
.card{text-align:center;height:458px;position:relative}
.card+.card::before{content:"";position:absolute;left:-19px;top:345px;height:80px;border-left:1px solid var(--rule)}
.card .photo{height:315px}
.card h3{font-size:14px;font-weight:700;text-transform:uppercase;margin-top:30px}
.card p{font-size:12px;color:var(--muted);line-height:1.4;margin:10px auto 0;width:180px}

.testimonials{position:relative;height:527px;background:linear-gradient(180deg,#6d7c4f 0%,#4a5d2d 50%,#3a3425 100%)}
.quote-panel{position:absolute;left:133px;top:0;width:367px;height:527px;background:rgba(125,181,51,.93);padding:30px 40px}
.quote{color:var(--white);margin-bottom:32px}
.quote .mark{font-family:Georgia,serif;font-size:34px;line-height:.6;display:block}
.quote h4{font-size:15px;font-weight:700;text-transform:uppercase;line-height:1.3;margin-top:6px}
.quote p{font-size:11px;line-height:1.4;opacity:.9;margin-top:6px}
.quote .who{font-size:10px;font-weight:600;text-transform:uppercase;margin-top:4px}

.welcome{height:451px;text-align:center;padding-top:90px}
.welcome h4{font-size:20px;font-weight:700;text-transform:uppercase}
.welcome h2{font-size:32px;font-weight:700;text-transform:uppercase;margin-top:12px}
.welcome p{font-size:15px;color:var(--muted);line-height:1.45;width:620px;margin:22px auto 34px}

.tile-grid{display:grid;grid-template-columns:repeat(4,300px);grid-auto-rows:344px}
.tile{padding:50px 30px;color:var(--white)}
.tile h3{font-size:20px;font-weight:700;text-transform:uppercase;margin-bottom:16px}
.tile p{font-size:12px;line-height:1.45;margin-bottom:18px}
.tile .lead{font-family:Montserrat,Arial,sans-serif;font-size:20px;font-weight:700;line-height:1.3}
.tile-blog{background:var(--green-dark);padding-top:100px}
.tile-news{background:var(--charcoal)}
.tile-vision{background:var(--green)}
.tile-mission{background:var(--teal)}

.site-footer{position:relative;height:562px;background:var(--white)}
.footer-art{position:absolute;left:0;top:20px;width:393px;height:540px;background:radial-gradient(circle at 45% 35%,#4fae87 0%,#2f8c67 45%,rgba(255,255,255,0) 72%)}
.footer-col{position:absolute;top:70px}
.footer-col h4{font-size:14px;font-weight:700;text-transform:uppercase;margin-bottom:14px}
.footer-col p,.footer-col li{font-size:11px;line-height:1.55;color:var(--ink);list-style:none}
.col-products{left:380px}
.col-contact{left:660px}
.col-follow{left:960px}
.social{display:flex;gap:8px}
.social span{width:26px;height:26px;border-radius:50%;background:var(--green-dark)}
.newsletter{position:absolute;left:440px;top:297px;width:410px}
.newsletter h4{font-size:14px;font-weight:700;text-transform:uppercase;margin-bottom:20px}
.newsletter .field{height:36px;border:1px solid var(--rule);font-size:11px;color:var(--muted);padding:10px 14px}
.newsletter .btn{display:block;text-align:center;margin-top:14px;font-size:18px;padding:10px}
.copyright{position:absolute;left:0;right:0;top:520px;text-align:center;font-size:10px;color:var(--muted)}
</style>
</head>
<body>

<header class="site-header">
  <div class="brand"><span class="brand-dot"></span><span class="brand-name">Tillard Environmental Projects</span></div>
  <nav class="nav">
    <a class="active" href="#">Home</a><a href="#">Who we are ▾</a><a href="#">Services ▾</a><a href="#">Products ▾</a><a href="#">News ▾</a><a href="#">Contact</a>
  </nav>
</header>

<section class="hero" role="img" aria-label="Apartment towers covered in vertical gardens against a cloudy sky">
  <div class="hero-box">
    <h1>Environmental<br>Projects</h1>
    <a class="btn" href="#" style="margin-top:14px;padding:8px 16px;font-size:12px">Read more ›</a>
  </div>
  <div class="hero-dots"><span></span><span></span><span class="on"></span><span></span><span></span></div>
</section>

<section class="services band">
  <h2 class="section-title">Our Services</h2>
  <div class="card-grid">
    <div class="card"><div class="photo" role="img" aria-label="Rows of green crops in a field" style="background:linear-gradient(180deg,#9cc0dd,#6a9b3a 45%,#3d6b22)"></div><h3>Sustainable Food</h3><p>Lorem Ipsum is simply dummy text of the printing and.</p></div>
    <div class="card"><div class="photo" role="img" aria-label="Flowering eco garden with shrubs" style="background:linear-gradient(160deg,#c86a8a,#5b8c3c 55%,#2f5a24)"></div><h3>Eco Gardens</h3><p>Lorem Ipsum is simply dummy text of the printing and.</p></div>
    <div class="card"><div class="photo" role="img" aria-label="Aerial view of aquaculture ponds" style="background:linear-gradient(180deg,#a8c08a,#7c9860 50%,#5b7046)"></div><h3>Aquaculture</h3><p>Lorem Ipsum is simply dummy text of the printing and.</p></div>
    <div class="card"><div class="photo" role="img" aria-label="Fish farm net pens in dark water" style="background:linear-gradient(180deg,#2f6a6a,#1b4a50)"></div><h3>Green Walls</h3><p>Lorem Ipsum is simply dummy text of the printing and.</p></div>
  </div>
  <div class="card-grid" style="margin-top:0">
    <div class="card"><div class="photo" role="img" aria-label="Raised garden bed with stone wall" style="background:linear-gradient(180deg,#4e7a34,#8a7a5a)"></div><h3>Sustainable Food</h3><p>Lorem Ipsum is simply dummy text of the printing and.</p></div>
    <div class="card"><div class="photo" role="img" aria-label="School of fish in blue water" style="background:linear-gradient(180deg,#1f8fb8,#0f5f8a)"></div><h3>Eco Gardens</h3><p>Lorem Ipsum is simply dummy text of the printing and.</p></div>
    <div class="card"><div class="photo" role="img" aria-label="Ripening tomatoes on the vine" style="background:linear-gradient(160deg,#2f5a22,#c0442a 55%,#7a2a18)"></div><h3>Aquaculture</h3><p>Lorem Ipsum is simply dummy text of the printing and.</p></div>
    <div class="card"><div class="photo" role="img" aria-label="Building facade with planted green wall" style="background:linear-gradient(90deg,#7e9a78,#4f7a44 50%,#b7c2b6)"></div><h3>Green Walls</h3><p>Lorem Ipsum is simply dummy text of the printing and.</p></div>
  </div>
</section>

<section class="products">
  <h2 class="section-title">Our Products</h2>
  <div class="card-grid">
    <div class="card"><div class="photo" role="img" aria-label="Fresh carrots pulled from soil" style="background:linear-gradient(180deg,#9ecf6a,#d2803a 55%,#4a3424)"></div><h3>Sustainable Food</h3><p>Lorem Ipsum is simply dummy text of the printing and.</p></div>
    <div class="card"><div class="photo" role="img" aria-label="Brick path through a lush garden" style="background:linear-gradient(180deg,#d9e6f0,#5e9444 40%,#8a8676)"></div><h3>Eco Gardens</h3><p>Lorem Ipsum is simply dummy text of the printing and.</p></div>
    <div class="card"><div class="photo" role="img" aria-label="Round fish farm enclosures at sea" style="background:linear-gradient(180deg,#7fc2dc,#2a8eb0 50%,#1f6c88)"></div><h3>Aquaculture</h3><p>Lorem Ipsum is simply dummy text of the printing and.</p></div>
    <div class="card"><div class="photo" role="img" aria-label="Ivy-covered building wall" style="background:linear-gradient(90deg,#4f6e34,#3c5a2a 70%,#c9ced4)"></div><h3>Green Walls</h3><p>Lorem Ipsum is simply dummy text of the printing and.</p></div>
  </div>
  <div class="card-grid" style="margin-top:0">
    <div class="card"><div class="photo" role="img" aria-label="Planter pockets mounted on a wall" style="background:linear-gradient(180deg,#e4ddd0,#6a8e3c 50%,#3a3a2c)"></div><h3>Living Food Walls</h3><p>Lorem Ipsum is simply dummy text of the printing and.</p></div>
    <div class="card"><div class="photo" role="img" aria-label="Trays of seedlings in a hydroponic greenhouse" style="background:linear-gradient(180deg,#3c6a2a,#7cb444 60%,#4e8a2c)"></div><h3>Hydroponic Gardens</h3><p>Lorem Ipsum is simply dummy text of the printing and.</p></div>
    <div class="card"><div class="photo" role="img" aria-label="Farm rows stretching to the horizon" style="background:linear-gradient(180deg,#a9c6dc,#6e9a48 45%,#7a6440)"></div><h3>Syndicated Farms</h3><p>Lorem Ipsum is simply dummy text of the printing and.</p></div>
    <div class="card"><div class="photo" role="img" aria-label="Barramundi fish close-up" style="background:linear-gradient(160deg,#24282a,#6c7270 55%,#2e3330)"></div><h3>Barramundi</h3><p>Lorem Ipsum is simply dummy text of the printing and.</p></div>
  </div>
</section>

<section class="testimonials" role="img" aria-label="Young green shoots growing in rows of soil">
  <div class="quote-panel">
    <div class="quote"><span class="mark">“</span><h4>Lorem ipsum is simply dummy text of the printing.</h4><p>There are many versions of passages of Lorem Ipsum available, but the</p><div class="who">Daniel</div></div>
    <div class="quote"><span class="mark">“</span><h4>Lorem ipsum is simply dummy text of the printing.</h4><p>There are many versions of passages of Lorem Ipsum available, but the</p><div class="who">Mara Holt</div></div>
    <div class="quote"><span class="mark">“</span><h4>Lorem ipsum is simply</h4><p>There are many versions of passages of Lorem Ipsum available, but the</p><div class="who">Owen</div></div>
  </div>
</section>

<section class="welcome band">
  <h4>Welcome to our site</h4>
  <h2>Tillard Environmental Projects.</h2>
  <p>Sed ut perspiciatis unde omnis iste natus error sit voluptatem accusantium doloremque laudantium, totam rem aperiam, eaque ipsa quae ab illo inventore veritatis et quasi architecto beatae vitae dicta sunt explicabo. Sed quia consequuntur magni dolores eos qui ratione voluptatem sequi nesciunt. Neque porro quisquam est.</p>
  <a class="btn" href="#">Read more</a>
</section>

<section class="tile-grid">
  <div class="tile" role="img" aria-label="Cabbages growing in a vegetable garden" style="background:linear-gradient(160deg,#8ab07a,#3d6a34)"></div>
  <div class="tile tile-blog"><h3>Latest Blog</h3><p class="lead">At vero eos et accusamus et iusto odio dignissimos</p></div>
  <div class="tile" role="img" aria-label="Garden path lined with colourful flowers" style="background:linear-gradient(160deg,#6a4a3a,#c0563a 50%,#4a6a2a)"></div>
  <div class="tile tile-news"><h3>News</h3><p>Sed ut perspiciatis unde omnis iste natus error sit voluptatem accusantium doloremque laudantium, totam rem aperiam, eaque ipsa quae ab illo inventore veritatis et.</p><a class="btn btn-small" href="#">Read more</a></div>
  <div class="tile tile-vision"><h3>Vision</h3><p>Our Vision is to make it easy for everyone to minimise their environmental impact by providing information, technology, packaged green solutions &amp; help, helping innovation flourish.</p><a class="btn btn-small" href="#">Read more</a></div>
  <div class="tile" role="img" aria-label="Greenhouse beds of leafy seedlings" style="background:linear-gradient(180deg,#2f4a22,#6ea43c)"></div>
  <div class="tile tile-mission"><h3>Mission</h3><p>Working with people to minimise the environmental impact of humans on the earth without sacrificing lifestyle and helping innovation flourish.</p><a class="btn btn-small" href="#">Read more</a></div>
  <div class="tile" role="img" aria-label="Hydroponic lettuce growing in white channels" style="background:linear-gradient(180deg,#d6ded4,#8ec07a 50%,#e6ebe4)"></div>
</section>

<footer class="site-footer">
  <div class="footer-art" role="img" aria-label="Illustration of a green tree with deer grazing beneath"></div>
  <div class="footer-col col-products">
    <h4>Products</h4>
    <ul><li>Sustainable Foods</li><li>Green walls</li><li>Eco gardens</li><li>Living food walls</li><li>Aquaculture – Fish Farm – Barramundi</li><li>Hydroponic gardens</li><li>Syndicated farms.</li></ul>
  </div>
  <div class="footer-col col-contact">
    <h4>Contact us</h4>
    <p>Unit 4, 18 Harbour Lane,<br>Sydney NSW 2000</p>
    <p style="margin-top:14px">info@tillardenvprojects.com</p>
  </div>
  <div class="footer-col col-follow">
    <h4>Follow us</h4>
    <div class="social"><span></span><span></span><span></span></div>
  </div>
  <div class="newsletter">
    <h4>Newsletter subscribe</h4>
    <div class="field">E-mail Address</div>
    <a class="btn" href="#">Join now</a>
  </div>
  <p class="copyright">Copyrights @ 2016 All Rights Reserved</p>
</footer>

</body>
</html>
```